Velvet & Vine by Mona
Text 410.582.3174 to set up and appointment
Instagram is Velvet_VineByMona
Location 4182 Carrow Ln. Notthingham Md, 21094 Suit 204
Slogan "Polished Looks. Radiant Days.
Specializing in pressicion cuts, blonding, fades, perms, waxing and more

The salon is black, gun metal color mirror with led lights. Green plants and has natural wood countertops for accent colors. Modern yet elegant. I want the card simple but it needs something to really grab the clients attention. I like black, grey, gold, green, natural tones and hints of pink or gold coloring
I’m open to anything. I don’t have a logo. Suggestions are welcome

Target Market(s)

20-60 men and woman

Industry/Entity Type

Hairstylist / barber

The name of the show should be bold. Maybe the letters could raised I also like foil for shine added or a mat finish

Colors

Requirements
Must have
• I also like some floral Floral designs, but not too overpowering. I like Sparkle, Watercolor design, Or a geometric line in the background
Nice to have
• I’m really here because I need creative help. I’m open for suggestions. I’ll post a picture of the salon in inspiration if I can find it.
Should not have
• Checkered background

```html
<!DOCTYPE html>
<html lang="en">
<head>
<meta charset="utf-8">
<title>Velvet &amp; Vine by Mona — Business Card</title>
<link href="https://fonts.googleapis.com/css2?family=Alex+Brush&family=Montserrat:wght@600&display=swap" rel="stylesheet">
<style>
  :root {
    --plum-deep: #3f0d2c;
    --plum: #6a1a48;
    --berry: #922f67;
    --cream-gold: #f4e6b6;
    --petal-light: #f3d6e4;
    --petal-mid: #dca2bf;
    --petal-deep: #b87096;
  }
  html, body {
    margin: 0;
    padding: 0;
    width: 1200px;
    height: 674px;
    overflow: hidden;
    background: var(--plum-deep);
  }
  .card {
    position: relative;
    width: 1200px;
    height: 674px;
    overflow: hidden;
    background:
      radial-gradient(ellipse at 85% 55%, rgba(178, 58, 128, 0.5), transparent 55%),
      radial-gradient(ellipse at 25% 75%, rgba(40, 5, 28, 0.5), transparent 55%),
      radial-gradient(ellipse at 50% 10%, rgba(40, 5, 28, 0.35), transparent 50%),
      linear-gradient(125deg, var(--plum-deep) 0%, var(--plum) 45%, var(--berry) 100%);
  }
  .floral-corner {
    position: absolute;
    left: -60px;
    top: -60px;
    width: 310px;
    height: 330px;
    border-radius: 40% 60% 55% 45% / 45% 40% 60% 55%;
    background: radial-gradient(circle at 36% 34%, var(--petal-light) 0%, var(--petal-mid) 45%, var(--petal-deep) 78%, rgba(184, 112, 150, 0.2) 100%);
  }
  .frame-lines, .sparkles {
    position: absolute;
    inset: 0;
  }
  .brand-mark {
    position: absolute;
    left: 231px;
    top: 221px;
    width: 222px;
    height: 222px;
    box-sizing: border-box;
    border: 3px solid var(--cream-gold);
    border-radius: 50%;
    display: flex;
    align-items: center;
    justify-content: center;
    text-align: center;
    font-family: "Montserrat", sans-serif;
    font-weight: 600;
    font-size: 31px;
    line-height: 1.15;
    letter-spacing: 1px;
    color: var(--cream-gold);
  }
  .divider {
    position: absolute;
    left: 515px;
    top: 229px;
    width: 4px;
    height: 190px;
    background: var(--cream-gold);
  }
  .business-name {
    position: absolute;
    left: 552px;
    top: 250px;
    margin: 0;
    font-family: "Alex Brush", cursive;
    font-weight: 400;
    font-size: 84px;
    line-height: 0.85;
    white-space: nowrap;
    color: var(--cream-gold);
    text-shadow: 0 2px 3px rgba(30, 4, 20, 0.65);
  }
  .business-name .byline {
    display: block;
    padding-left: 100px;
  }
  .slogan {
    position: absolute;
    left: 350px;
    top: 570px;
    margin: 0;
    font-family: "Alex Brush", cursive;
    font-size: 58px;
    line-height: 1;
    white-space: nowrap;
    word-spacing: 8px;
    color: var(--cream-gold);
    text-shadow: 0 2px 3px rgba(30, 4, 20, 0.65);
  }
</style>
</head>
<body>
  <main class="card">
    <div class="floral-corner" role="img" aria-label="Pink dahlia flower illustration in the top left corner"></div>

    <svg class="frame-lines" width="1200" height="674" viewBox="0 0 1200 674" aria-hidden="true">
      <polyline points="242,13 1187,13 1187,651 14,651 14,262" fill="none" stroke="var(--cream-gold)" stroke-width="3"/>
    </svg>

    <svg class="sparkles" width="1200" height="674" viewBox="0 0 1200 674" aria-hidden="true" fill="var(--cream-gold)">
      <defs>
        <path id="sparkle" d="M0,-1 C0.12,-0.12 0.12,-0.12 1,0 C0.12,0.12 0.12,0.12 0,1 C-0.12,0.12 -0.12,0.12 -1,0 C-0.12,-0.12 -0.12,-0.12 0,-1 Z"/>
      </defs>
      <use href="#sparkle" transform="translate(258,46) scale(14)"/>
      <use href="#sparkle" transform="translate(248,119) scale(14)"/>
      <use href="#sparkle" transform="translate(220,183) scale(14)"/>
      <use href="#sparkle" transform="translate(158,245) scale(14)"/>
      <use href="#sparkle" transform="translate(81,276) scale(14)"/>
      <use href="#sparkle" transform="translate(52,575) scale(14)"/>
      <use href="#sparkle" transform="translate(92,566) scale(10)"/>
      <use href="#sparkle" transform="translate(77,605) scale(26)"/>
    </svg>

    <div class="brand-mark">VELVET<br>&amp; VINE</div>
    <div class="divider"></div>

    <h1 class="business-name">Velvet &amp; Vine<span class="byline">by Mona</span></h1>

    <p class="slogan">Polished Looks Radiant Days</p>
  </main>
</body>
</html>
```